Window Graphics ‘Opening Soon’ for new Jewellery Boutique

We want to fully cover the shop window for a duration of 6 weeks whilst the refurbishment is going on. The window graphics should be cool, sexy and sophisticated. The graphics should include our company logo ‘THE COPPER LANTERN’ in Gills Sans Font. The shop will be an upmarket jewellery watch shop.

Target Market(s)

Jewellery customers

Industry/Entity Type

Jewellery

Colors

Designer to choose colors to be used in the design.

Requirements
Must have
• Must be loud graphics that catch your attention when walking past. I have provided a graphics example where the colour palette is black, white and shocking pink!
Nice to have
• The Boss is Back…. The Copper Lantern Proudly present a new masterpiece coming soon….

```html
<!DOCTYPE html>
<html lang="en">
<head>
<meta charset="utf-8">
<title>The Copper Lantern – Window Graphics</title>
<link rel="stylesheet" href="https://fonts.googleapis.com/css2?family=Cabin:wght@400;500;600&display=swap">
<style>
  :root {
    --page-bg: #f4f2ef;
    --ink-dark: #141014;
    --bronze-deep: #4a3022;
    --bronze: #8a6244;
    --tan: #a87e5a;
    --white: #ffffff;
  }
  html, body {
    margin: 0;
    width: 1200px;
    height: 900px;
    overflow: hidden;
    background: var(--page-bg);
  }
  .window-graphics {
    display: block;
    width: 1200px;
    height: 900px;
    font-family: "Cabin", sans-serif;
  }
  .headline, .tagline, .slogan, .slogan-side, .coming-soon, .door-name {
    fill: var(--white);
    text-anchor: middle;
  }
  .headline { font-size: 36px; font-weight: 400; }
  .tagline { font-size: 13px; font-weight: 400; }
  .slogan { font-size: 33px; font-weight: 500; }
  .slogan-side { font-size: 42px; font-weight: 500; }
  .coming-soon { font-size: 66px; font-weight: 600; }
  .door-name { font-size: 15px; font-weight: 500; letter-spacing: 1px; }
</style>
</head>
<body>
<svg class="window-graphics" viewBox="0 0 1200 900" xmlns="http://www.w3.org/2000/svg">
  <defs>
    <linearGradient id="sceneFill" x1="0" y1="0" x2="0" y2="1">
      <stop offset="0" stop-color="var(--ink-dark)"/>
      <stop offset="0.45" stop-color="var(--bronze-deep)"/>
      <stop offset="1" stop-color="var(--tan)"/>
    </linearGradient>
  </defs>

  <rect class="panel-side" x="40" y="211" width="181" height="477" fill="url(#sceneFill)"
        role="img" aria-label="Dark backdrop with the edge of a bronze display platform"/>
  <rect class="panel-main" x="249" y="211" width="703" height="477" fill="url(#sceneFill)"
        role="img" aria-label="Stage scene with bronze curtains, an oval gold-rimmed platform, a black jewellery bust and round display plinths"/>
  <rect class="panel-door" x="998" y="237" width="158" height="451" fill="url(#sceneFill)"
        role="img" aria-label="Dark backdrop with the edge of a bronze display platform"/>

  <g class="side-message">
    <text class="slogan-side" x="130" y="367">THE</text>
    <text class="slogan-side" x="130" y="424">BOSS</text>
    <text class="slogan-side" x="130" y="479">IS</text>
    <text class="slogan-side" x="130" y="536">BAC...</text>
  </g>

  <g class="main-message">
    <text class="headline" x="588" y="326">THE COPPER LANTERN</text>
    <text class="tagline" x="588" y="352">LUXURY JEWELLERY AND WATCHES</text>
    <text class="slogan" x="598" y="396">PROUDLY PRESENT NEW MASTERPIECE</text>
    <text class="coming-soon" x="594" y="550">COMING SOON...</text>
  </g>

  <g class="door-brand">
    <text class="door-name" x="1077" y="496">THE COPPER</text>
    <text class="door-name" x="1077" y="516">LANTERN</text>
  </g>
</svg>
</body>
</html>
```